【デザインテイストについて】
カジュアル・ゴージャス・にぎやか・ナチュラル・優しい・パステル
シンプル・清潔な・重厚感

【デザインカラーについて】
サロンの内装にレンガがあるのですが、私が直接施工してまして
それはもし可能であれば、サイトのデザイン内に組み込んで頂ければ
とても嬉しいです。

【参考にしているデザイン】
インテリア本:Den Lark Journal
本内のデザインや見せ方が好みです。
https://denlark.jp/cp/denlarkjournal

【その他】
●「http://velmora-salon.com/」のページ下部にあるlinkwave部分の様に
サイトの中に挿入したいと考えています。
見本で構いませんので、画像で貼り付けて頂ければ嬉しいです。

●サニーフォークに飛ばす物も良ければ配置してほしいです。

【ページ項目】
①トップページ
②サロン紹介
③スタッフ紹介
④お知らせ
⑤ブログ
⑥スタイルギャラリー
⑦コンセプト
⑧商品紹介
⑨よくある質問
⑩メニュー
⑪クーポン
⑫フリーマーケット
⑬レビュー投稿(お問い合わせのフォーム)
⑭お客様の声

http://beauty.sunnyfork.jp/slnK000918274/
1ページ
ベージュ、グリーン、茶色
• 高解像度JPG (.jpg)
• イラストレーター形式 (.ai)
• フォトショップ形式 (.psd)
• PNG形式 (.png)
----------------------------------------------------

【素材について】
※ロゴ
サロンのキャラクターがあるので、サイトの中で使って頂ければ幸いです。
http://cratebin.jp/download/9a7e3c10bd4f2e8a5c6d0b7f12e49a8c3d5f6e71
ダウンロードパスワード:qump4rtz

※サロン写真
http://cratebin.jp/download/2c8f1e6ab93d4705e1f6c2a8d0b5e7f3a9c4d186
ダウンロードパスワード:bol3wadq

※その他
グラニカ「https://jp.granica-stock.com/」の定期契約内の画像は使用可能です。
グラニカ以外は無料の素材をご使用くださいませ。

ゴールデンウィーク中で大変申し訳ありませんが、一週間延長させて頂きます。
是非宜しくお願い致します。

一目ぼれしました!
とても目を引くデザインで、当サロンのイラストをうまく取り込んで頂いていルなと思い、選ばせて頂きました!

沢山のご提案をして頂き、本当にありがとうございました!
とても嬉しく全てのデザインを使用したいところですが、コンペ形式にて1つしか選べないと言うのあとても心苦しく思っています。

またこのような機会がありましたら、ご協力頂けますと幸いです。
ありがとうございました。

```html
<!DOCTYPE html>
<html lang="ja">
<head>
<meta charset="utf-8">
<title>Velmora hair salon</title>
<link rel="stylesheet" href="https://fonts.googleapis.com/css2?family=Noto+Sans+JP:wght@400;700&family=Noto+Serif+JP:wght@500;700&family=Playfair+Display:wght@700&display=swap">
<style>
:root{
  --beige:#f4ede1;
  --beige-deep:#e6d8c2;
  --brown:#5b3a26;
  --brown-soft:#8a6a50;
  --red:#c23a2c;
  --green:#6e8c3c;
  --teal:#3f9a9a;
  --white:#ffffff;
  --ink:#3b2d24;
  --line:#d6c6ae;
}
*{box-sizing:border-box;margin:0;padding:0}
html,body{width:723px;height:1200px;overflow:hidden}
body{font-family:"Noto Sans JP",sans-serif;color:var(--ink);background:var(--beige);font-size:8px;line-height:1.5}
.page{width:723px;height:1200px;position:relative}

/* header */
.site-header{height:50px;display:flex;align-items:center;justify-content:space-between;padding:0 56px;background:var(--white)}
.brand{display:flex;align-items:center;gap:6px}
.brand-dot{width:14px;height:14px;border-radius:50%;background:var(--red)}
.brand-name{font-family:"Noto Sans JP",sans-serif;font-weight:700;font-size:20px;color:var(--red)}
.brand-tag{font-size:7px;color:var(--brown-soft);margin-left:6px}
.header-contact{text-align:right;color:var(--brown)}
.header-contact .addr{font-size:6.5px}
.tel{font-size:16px;font-weight:700;color:var(--red);letter-spacing:.5px}
.tel small{font-size:8px;margin-right:3px}

.global-nav{height:28px;background:var(--beige);border-top:2px solid var(--red);border-bottom:1px solid var(--line);display:flex;justify-content:center;gap:38px;align-items:center}
.global-nav a{font-family:"Playfair Display",serif;font-size:9px;color:var(--red);text-decoration:none;letter-spacing:1px}

/* hero */
.hero{height:175px;background:linear-gradient(100deg,#3d2a1e 0%,#7a5636 30%,#b49170 55%,#d8c4a5 80%,#a98b6c 100%)}

/* concept */
.concept{height:287px;background:var(--beige);text-align:center;padding-top:14px}
.section-label{font-family:"Playfair Display",serif;font-size:9px;color:var(--red);letter-spacing:1px}
.section-label span{font-family:"Noto Sans JP",sans-serif;font-size:6.5px;color:var(--brown-soft);margin-left:4px}
.concept-title{font-family:"Playfair Display",serif;font-size:24px;color:var(--brown);margin:4px 0 6px}
.concept-visual{display:flex;justify-content:center;align-items:flex-end;gap:14px;height:80px}
.concept-visual .side{width:150px;height:54px;background:linear-gradient(180deg,#e9c6a8,#c98f67)}
.concept-visual .photo{width:120px;height:80px;background:linear-gradient(160deg,#e0cbb0,#9c7556)}
.concept-lead{font-family:"Noto Serif JP",serif;font-size:10px;color:var(--brown);margin:14px 0 8px;font-weight:700}
.concept-body{font-size:6.5px;color:var(--brown-soft);width:420px;margin:0 auto;line-height:1.9}
.btn{display:inline-block;border:1px solid var(--brown-soft);background:var(--white);color:var(--brown);font-size:6.5px;padding:3px 18px;margin-top:10px}

/* content grid */
.contents{height:290px;background:linear-gradient(180deg,#e5dace,#d9cab8);padding:18px 0}
.card-grid{width:430px;margin:0 auto;display:grid;grid-template-columns:repeat(3,1fr);gap:16px 20px}
.card-head{font-family:"Playfair Display",serif;font-size:9px;color:var(--red);border-bottom:1px solid var(--brown-soft);margin-bottom:4px}
.card-head span{font-family:"Noto Sans JP",sans-serif;font-size:6px;color:var(--brown);margin-left:3px}
.card-img{height:68px}
.card .btn{display:block;margin:5px auto 0;width:80px;text-align:center;padding:2px 0}

/* banners */
.feature-row{width:430px;margin:14px auto 0;display:grid;grid-template-columns:1fr 1fr;gap:12px}
.banner{height:36px;display:flex;align-items:center;justify-content:center;flex-direction:column;color:var(--white)}
.banner.qa{background:linear-gradient(90deg,#bfb3a4,#ece4d7);color:var(--brown)}
.banner.market{background:var(--brown-soft)}
.banner strong{font-family:"Playfair Display",serif;font-size:17px;letter-spacing:1px}
.banner small{font-size:6px}

.news{margin-top:10px;background:var(--white);padding:6px 8px;height:108px}
.news h3{font-family:"Playfair Display",serif;font-size:10px;color:var(--brown);text-align:center}
.news h3 span{font-family:"Noto Sans JP",sans-serif;font-size:6px;margin-left:3px}
.news li{list-style:none;font-size:6px;border-bottom:1px dotted var(--line);padding:3px 0}
.news .btn{display:block;width:70px;margin:5px auto 0;text-align:center;padding:2px 0}

.feed{margin-top:10px;background:var(--white);border:1px solid var(--line);height:134px;padding:6px 8px;overflow:hidden}
.feed-head{display:flex;gap:6px;align-items:center;border-bottom:1px solid var(--line);padding-bottom:4px}
.feed-head .thumb{width:20px;height:20px;background:linear-gradient(135deg,#d9b48f,#8b6547)}
.feed-head b{font-size:7px;color:var(--brown)}
.feed-post{display:flex;gap:6px;align-items:center;padding:4px 0;border-bottom:1px solid #eee}
.feed-post:last-child{border-bottom:none}
.feed-post .thumb{width:28px;height:22px;flex:none;background:linear-gradient(135deg,#e6d6c1,#b69675)}
.feed-post p{font-size:6px;color:var(--brown-soft)}

.link-row{width:430px;margin:10px auto 0;display:grid;grid-template-columns:1fr 1fr;gap:12px}
.link-btn{height:30px;display:flex;align-items:center;justify-content:center;gap:6px;color:var(--white);font-size:8px;font-weight:700}
.link-btn.booking{background:var(--brown)}
.link-btn.coupon{background:var(--teal)}

/* footer */
.site-footer{position:absolute;left:0;top:1068px;width:723px;height:132px;background:var(--white)}
.footer-inner{width:540px;margin:0 auto;display:flex;gap:18px;padding-top:14px}
.footer-art{width:60px;height:90px;background:linear-gradient(180deg,#f1b8b8,#c98060)}
.footer-info{width:160px;color:var(--brown)}
.footer-info .brand-name{font-size:16px}
.footer-info p{font-size:6px;line-height:1.7}
.footer-info .tel{font-size:13px}
.footer-links{display:grid;grid-template-columns:repeat(3,1fr);gap:2px 16px;flex:1;align-content:start;padding-top:10px}
.footer-links a{font-size:6px;color:var(--brown);text-decoration:none}
.footer-links a::before{content:"▶";color:var(--red);font-size:4px;margin-right:3px;vertical-align:middle}
.footer-mascot{width:40px;height:44px;border-radius:50%;background:linear-gradient(135deg,#5e8e52,#2f5234);align-self:flex-end}
.copyright{position:absolute;bottom:0;left:0;width:100%;height:12px;background:var(--brown);color:var(--white);font-size:5.5px;text-align:center;line-height:12px}
</style>
</head>
<body>
<div class="page">
  <header class="site-header">
    <div class="brand">
      <span class="brand-dot"></span>
      <span class="brand-name">Velmora</span>
      <span class="brand-tag">上質なひとときをあなたの特別な空間で</span>
    </div>
    <div class="header-contact">
      <p class="addr">神奈川県横浜市青葉区みどり台2-14-8 / 営業 9:00〜19:00</p>
      <p class="tel"><small>TEL</small>045-812-3304</p>
    </div>
  </header>
  <nav class="global-nav">
    <a>CONCEPT</a><a>MENU</a><a>SALON</a><a>GALLERY</a><a>VOICE</a><a>STAFF</a><a>PRODUCT</a><a>BLOG</a>
  </nav>

  <div class="hero" role="img" aria-label="Salon entrance photo with an OPEN sign board, brick wall and the salon's mascot characters"></div>

  <section class="concept">
    <p class="section-label">CONCEPT<span>サロンコンセプト</span></p>
    <h2 class="concept-title">「Private Salon」</h2>
    <div class="concept-visual">
      <div class="side" role="img" aria-label="Brick wall with the salon's bird mascot"></div>
      <div class="photo" role="img" aria-label="Photo of the two salon stylists"></div>
      <div class="side" role="img" aria-label="Brick wall with the salon's second bird mascot"></div>
    </div>
    <p class="concept-lead">お客様の居心地のよいオシャレを空間と、それぞれに寄り添う完全プライベートな美容室です。</p>
    <p class="concept-body">手作りのレンガに囲まれた落ち着いた空間で、お一人おひとりに合わせた施術をご提供しています。ゆったりと流れる時間の中で、日常を忘れてくつろいでいただけるよう、スタッフ一同心を込めてお迎えいたします。</p>
    <span class="btn">コンセプトの詳細はこちら</span>
  </section>

  <section class="contents">
    <div class="card-grid">
      <div class="card"><p class="card-head">MENU<span>メニュー</span></p><div class="card-img" role="img" aria-label="Photo of the salon menu board" style="background:linear-gradient(135deg,#cdb698,#7d5c41)"></div><span class="btn">MENU詳細</span></div>
      <div class="card"><p class="card-head">SALON<span>サロン紹介</span></p><div class="card-img" role="img" aria-label="Photo of the salon interior" style="background:linear-gradient(135deg,#b9a48b,#5d4736)"></div><span class="btn">SALON詳細</span></div>
      <div class="card"><p class="card-head">GALLERY<span>ギャラリー</span></p><div class="card-img" role="img" aria-label="Photo of a hairstyle model" style="background:linear-gradient(135deg,#e1cdb8,#8e6a50)"></div><span class="btn">GALLERY詳細</span></div>
      <div class="card"><p class="card-head">VOICE<span>お客様の声</span></p><div class="card-img" role="img" aria-label="Photo of a stylist at work" style="background:linear-gradient(135deg,#d8c8b6,#6e5644)"></div><span class="btn">VOICE詳細</span></div>
      <div class="card"><p class="card-head">PRODUCT<span>商品紹介</span></p><div class="card-img" role="img" aria-label="Photo of hair care products" style="background:linear-gradient(135deg,#f0e6da,#b69c80)"></div><span class="btn">PRODUCT詳細</span></div>
      <div class="card"><p class="card-head">BLOG<span>ブログ</span></p><div class="card-img" role="img" aria-label="Photo of a smiling client" style="background:linear-gradient(135deg,#e7d3bf,#a07d62)"></div><span class="btn">BLOG詳細</span></div>
    </div>
  </section>

  <div class="feature-row">
    <div>
      <div class="banner qa"><strong>Q&amp;A</strong><small>よくある質問</small></div>
      <div class="news">
        <h3>NEWS<span>お知らせ</span></h3>
        <ul>
          <li>2024.05.10 ゴールデンウィーク営業のお知らせ</li>
          <li>2024.04.22 新メニューを追加しました</li>
          <li>2024.04.01 春のキャンペーン開始</li>
        </ul>
        <span class="btn">一覧を見る</span>
      </div>
    </div>
    <div>
      <div class="banner market"><strong>FREE MARKET</strong><small>フリーマーケット</small></div>
      <div class="feed">
        <div class="feed-head"><span class="thumb" role="img" aria-label="Salon profile photo"></span><b>Velmora linkwave</b></div>
        <div class="feed-post"><span class="thumb" role="img" aria-label="Market item photo"></span><p>手作り雑貨を出品しました。ぜひご覧ください。</p></div>
        <div class="feed-post"><span class="thumb" role="img" aria-label="Market item photo"></span><p>ヘアアクセサリー入荷しました。数量限定です。</p></div>
        <div class="feed-post"><span class="thumb" role="img" aria-label="Market item photo"></span><p>来月のマーケット開催日が決まりました。</p></div>
      </div>
    </div>
  </div>

  <div class="link-row">
    <div class="link-btn booking">サニーフォークでご予約 ▶</div>
    <div class="link-btn coupon">クーポン情報はこちら ▶</div>
  </div>

  <footer class="site-footer">
    <div class="footer-inner">
      <div class="footer-art" role="img" aria-label="Illustration of the salon mascot sitting in a styling chair"></div>
      <div class="footer-info">
        <span class="brand-name">Velmora</span>
        <p>〒227-0044 神奈川県横浜市青葉区みどり台2-14-8</p>
        <p class="tel"><small>TEL</small>045-812-3304</p>
        <p>営業時間 9:00〜19:00 / 定休日 毎週火曜日</p>
      </div>
      <div class="footer-links">
        <a>トップページ</a><a>サロン紹介</a><a>スタッフ紹介</a>
        <a>お知らせ</a><a>ブログ</a><a>スタイルギャラリー</a>
        <a>コンセプト</a><a>商品紹介</a><a>よくある質問</a>
        <a>メニュー</a><a>クーポン</a><a>フリーマーケット</a>
        <a>レビュー投稿</a><a>お客様の声</a>
      </div>
      <div class="footer-mascot" role="img" aria-label="Small mascot character illustration"></div>
    </div>
    <p class="copyright">© Velmora hair salon All Rights Reserved.</p>
  </footer>
</div>
</body>
</html>
```